Fennel Cellar Online organic artisan and gourmet supermarket

Brief:
Brand: Fennel Cellar (FC) is an online store selling artisan and organinc Italian products. Our look and feel we have gone with is rustic, premium and unfiltered (visit us @ www.fennelcellar.com.au)
Our slogan: "shop fresh, cook slow, share often"
Goals: prior to our online store going live, we used to attend a food market once a week. Due to unfortunate circumstances, we stopped. Since then, our store has gone live and wanted to use the card as a reminder we are back at the markets.
I also have a restaurant, "fennel ristorante" so I wanted to hand them out to customers in the restaurant but also act as reminder of our pop up market stores and our website to buy from.
Personality: FC is more than just a store. Our goal is to be not only a store but an informationa hub of Italian food.
We offer assistance to people who need help in their kitchen as well as catering
Logo: I have a logo which I was not able to upload.

Target Market(s)

Food lovers
Italian food interest
Wealthy
Organic gourmet food enthusiest

Industry/Entity Type

Store

Contact Information for Business Card

Shop online or visit us @ Willow Bend organic market
Ciao@fennelcellar.com.au
Www.fennelcellar.com.au

Online store, Cooking advice, catering, ristorante and information hub

Requirements
Must have
• Logo
• Information
• May be larger than a business card to fit information but smaller than a post card
• Need to look interesting and different
• Not a simple card design
Nice to have
• Different fonts
• Rustic looking
• Qwerky

```html
<!DOCTYPE html>
<html lang="en">
<head>
<meta charset="utf-8">
<title>Fennel Cellar – Business Card</title>
<link href="https://fonts.googleapis.com/css2?family=Source+Sans+3:ital,wght@0,400;0,600;0,700;1,700&display=swap" rel="stylesheet">
<style>
  :root {
    --bg: #ecebe8;
    --card-white: #ffffff;
    --brand-red: #cc0020;
    --brand-green: #017a33;
    --ink: #222222;
    --on-red: #ffffff;
  }
  * { margin: 0; padding: 0; box-sizing: border-box; }
  html, body {
    width: 1200px; height: 900px; overflow: hidden;
    background: var(--bg);
    font-family: "Source Sans 3", "Myriad Pro", Arial, sans-serif;
  }
  .canvas { position: relative; width: 1200px; height: 900px; }

  /* Front of card */
  .card-front {
    position: absolute; left: 78px; top: 34px;
    width: 588px; height: 364px;
    background: var(--card-white);
    overflow: hidden;
    box-shadow: 0 6px 18px rgba(0,0,0,.18);
  }
  .card-front .bands { position: absolute; inset: 0; }
  .brand-mark {
    position: absolute; left: 225px; top: 20px;
    width: 160px; height: 160px;
    border: 2px solid var(--ink); border-radius: 50%;
    display: flex; align-items: center; justify-content: center;
  }
  .brand-name {
    color: var(--ink); font-weight: 600; font-size: 19px;
    letter-spacing: 1px; text-transform: uppercase; text-align: center;
    line-height: 1.15;
  }
  .contact {
    position: absolute; right: 270px; top: 244px;
    color: var(--on-red); font-size: 17px; line-height: 24px;
    text-align: right;
  }
  .contact-line { display: flex; align-items: center; justify-content: flex-end; gap: 6px; }
  .contact-line svg { width: 13px; height: 13px; }
  .person { position: absolute; left: 348px; top: 244px; color: var(--on-red); }
  .person-name { font-weight: 600; font-size: 23px; line-height: 28px; }
  .person-role { font-size: 17px; line-height: 22px; }
  .slogan {
    position: absolute; left: 0; right: 0; top: 312px;
    text-align: center; color: var(--on-red);
    font-style: italic; font-weight: 700; font-size: 17px;
    padding-left: 14px;
  }

  /* Back of card */
  .card-back {
    position: absolute; left: 388px; top: 505px;
    width: 567px; height: 352px;
    background: var(--brand-red);
    color: var(--on-red); text-align: center;
    box-shadow: 0 6px 18px rgba(0,0,0,.18);
  }
  .invite {
    position: absolute; left: 50px; right: 50px; top: 116px;
    font-weight: 600; font-size: 21px; line-height: 30px;
    text-transform: uppercase;
  }
  .services {
    position: absolute; left: 40px; right: 40px; top: 225px;
    font-weight: 600; font-size: 16.5px; line-height: 24px;
  }
  .dot { display: inline-block; width: 7px; height: 7px; border-radius: 50%;
         background: var(--on-red); margin: 0 8px; vertical-align: middle; }
</style>
</head>
<body>
<main class="canvas">

  <section class="card-front" aria-label="Business card front">
    <svg class="bands" width="588" height="364" viewBox="0 0 588 364" aria-hidden="true">
      <polygon points="414,195 588,195 588,364 0,364 0,229 392,229" fill="var(--brand-red)"/>
      <polygon points="0,203 400,203 381,229 0,229" fill="var(--brand-green)"/>
    </svg>

    <div class="brand-mark">
      <span class="brand-name">Fennel<br>Cellar</span>
    </div>

    <div class="contact">
      <div class="contact-line">Ciao@fennelcellar.com.au
        <svg viewBox="0 0 13 13" aria-hidden="true"><rect x="1" y="3" width="11" height="8" fill="#fff"/><polyline points="1,3 6.5,7.5 12,3" fill="none" stroke="var(--brand-red)" stroke-width="1.2"/></svg>
      </div>
      <div class="contact-line">Www.fennelcellar.com.au
        <svg viewBox="0 0 13 13" aria-hidden="true"><circle cx="6.5" cy="6.5" r="5.5" fill="#fff"/><path d="M4 4 L6 5 L5 8 Z M8 6 L10 8 L8 10 Z" fill="var(--brand-red)"/></svg>
      </div>
    </div>

    <div class="person">
      <div class="person-name">Luca Ferrante</div>
      <div class="person-role">Managing Director</div>
    </div>

    <p class="slogan">"shop fresh, cook slow, share often"</p>
  </section>

  <section class="card-back" aria-label="Business card back">
    <p class="invite">Shop online or visit us @ Willow Bend organic market</p>
    <p class="services">Web shop<span class="dot"></span>Kitchen help<span class="dot"></span>Event catering<br>Ristorante and Food Info Hub</p>
  </section>

</main>
</body>
</html>
```